Tri fold brochure for construction company

Looking for a tri fold brochure which utilizes black, teal and white colors. Logo must be on main page (several files with Logo attached)
Inside brochure.
1st Page - 3D photo/sketch/drawing of a complete residential high rise building with windows, balconies and elements of concrete and bricks.
2nd Page - Text which will outline company's main activities. file with text is attached.
3rd Page - photo/sketch/drawing of underground parking garage which shows columns/beams/walls/ and garage entrance/exit ramp. Can be multiple photos.
Back of brochure
1st page - company logo
2nd page - please propose something.
3rd page - company message with address and contact info (to be provided)
Back ground color of brochure should complement our logo/photos/sketches/drawings.
Alternative design options are welcome.

```html
<!DOCTYPE html>
<html lang="en">
<head>
<meta charset="utf-8">
<title>Meridian Restoration Corp – Tri-fold Brochure</title>
<link href="https://fonts.googleapis.com/css2?family=Lato:wght@400;700;900&display=swap" rel="stylesheet">
<style>
  :root{
    --teal:#1fb39a;
    --teal-dark:#15927d;
    --black:#141414;
    --ink:#2b2b2b;
    --grey:#6b6b6b;
    --paper:#ffffff;
    --stage:#dcdcdc;
  }
  *{box-sizing:border-box;margin:0;padding:0}
  html,body{width:759px;height:1200px;overflow:hidden}
  body{background:var(--stage);font-family:"Lato",sans-serif;color:var(--ink);position:relative}
  .spread{position:absolute;left:35px;width:690px;height:540px;background:var(--paper);display:flex;box-shadow:0 4px 14px rgba(0,0,0,.18)}
  .spread--outside{top:40px}
  .spread--inside{top:620px}
  .panel{position:relative;width:230px;height:540px;overflow:hidden}
  .panel + .panel{border-left:1px solid #eee}
  .shape{position:absolute;left:0;top:0;width:230px;height:540px}
  .photo{position:absolute}
  .brand{position:absolute;display:flex;align-items:center;gap:8px;color:#fff;font-weight:900;font-size:19px;letter-spacing:1px}
  .brand__mark{width:16px;height:16px;background:var(--teal)}
  .brand small{display:block;font-size:7px;font-weight:700;letter-spacing:1.5px;margin-top:1px}
  .heading{font-weight:900;line-height:1.1}
  .heading--teal{color:var(--teal)}
  .body-copy{font-size:8px;line-height:1.45;color:var(--grey)}

  /* outside: about */
  .about__photo{left:0;top:0;width:230px;height:180px;background:linear-gradient(160deg,#9aa7b3,#4d5e72 55%,#c9a44a)}
  .about__title{position:absolute;left:20px;top:212px;font-size:20px;color:var(--teal-dark)}
  .about__text{position:absolute;left:20px;top:244px;width:190px}
  .about__city{left:0;top:395px;width:230px;height:145px;background:linear-gradient(170deg,#6a5a3f,#3a3328 60%,#2a2520)}
  .about .brand{left:28px;top:460px}

  /* outside: contact */
  .contact__message{position:absolute;left:30px;top:70px;width:180px}
  .contact__message .heading--teal{font-size:19px}
  .contact__message .heading--dark{font-size:19px;color:var(--black)}
  .contact__list{position:absolute;left:30px;top:160px;list-style:none}
  .contact__list li{display:flex;align-items:center;gap:10px;font-size:9px;margin-bottom:14px;color:var(--ink)}
  .icon{width:20px;height:20px;border-radius:50%;background:var(--teal);display:flex;align-items:center;justify-content:center;flex:none}
  .icon svg{width:11px;height:11px}
  .contact__map{left:0;top:360px;width:230px;height:180px;background:linear-gradient(180deg,#f5f5f5,#e6e6e6)}

  /* outside: cover */
  .cover .brand{left:24px;top:55px;font-size:20px}
  .cover__photo{left:0;top:150px;width:230px;height:240px;background:linear-gradient(180deg,#c7c9c6,#8f8a7a 45%,#5d5548)}
  .cover__headline{position:absolute;left:0;width:230px;top:410px;text-align:center}
  .cover__headline .heading--teal{font-size:20px}
  .cover__headline .heading--dark{font-size:20px;color:var(--black)}
  .cover__web{position:absolute;left:0;bottom:0;width:230px;height:34px;background:var(--teal);color:#fff;font-size:9px;font-weight:700;display:flex;align-items:center;justify-content:center}

  /* inside: intro */
  .intro__text{position:absolute;left:18px;top:22px;width:196px;color:#fff}
  .intro__text .body-copy{color:#eafaf6}
  .intro__building{left:0;top:200px;width:230px;height:340px;background:linear-gradient(180deg,#dfe6ea,#b9c7cf 40%,#4f6f7d 75%,#3e5f3a)}

  /* inside: services */
  .section-title{font-size:14px;color:var(--teal-dark);text-align:center;margin-bottom:8px}
  .services{padding:20px 10px 0}
  .services__group{margin-bottom:16px}
  .services__cols{display:flex;gap:8px}
  .services__col{flex:1}
  .pill{display:block;background:var(--teal);color:#fff;font-size:7px;font-weight:700;text-transform:uppercase;padding:3px 6px;border-radius:10px;margin-bottom:5px}
  .item{display:flex;gap:4px;font-size:7.5px;line-height:1.25;color:var(--ink);margin-bottom:4px}
  .item__num{width:12px;height:12px;border-radius:50%;border:1.5px solid var(--teal);color:var(--teal-dark);font-size:6px;font-weight:900;display:flex;align-items:center;justify-content:center;flex:none}

  /* inside: misc */
  .misc{padding:22px 16px 0}
  .misc .section-title{text-align:left;color:var(--black)}
  .misc__list{list-style:none}
  .misc__list li{font-size:7.5px;color:var(--ink);padding-left:10px;position:relative;margin-bottom:4px}
  .misc__list li::before{content:"";position:absolute;left:0;top:3px;width:5px;height:5px;background:var(--teal);border-radius:50%}
  .misc__photo{left:0;top:150px;width:230px;height:190px;background:linear-gradient(180deg,#c8c8c8,#8b8b8b 50%,#3b3b3b)}
  .misc__text{position:absolute;left:16px;top:360px;width:170px}
</style>
</head>
<body>

<!-- Outside of the brochure -->
<section class="spread spread--outside">
  <div class="panel about">
    <div class="photo about__photo" role="img" aria-label="Photo of a contractor wearing a tool belt and carrying a power tool"></div>
    <svg class="shape" viewBox="0 0 230 540" aria-hidden="true">
      <polygon points="0,150 230,180 230,200 0,178" fill="var(--teal)"/>
      <polygon points="0,178 230,200 230,210 0,210" fill="#fff"/>
    </svg>
    <h2 class="heading about__title">About Us</h2>
    <p class="body-copy about__text">We are a restoration firm serving residential towers, plazas and parking structures. Our crews repair concrete, seal envelopes and protect buildings for decades. Every project is planned with care, delivered on schedule and backed by trusted warranties for owners.</p>
    <div class="photo about__city" role="img" aria-label="Aerial photo of a city at dusk"></div>
    <svg class="shape" viewBox="0 0 230 540" aria-hidden="true">
      <polygon points="0,380 230,395 230,405 0,398" fill="var(--teal)"/>
    </svg>
    <div class="brand"><span class="brand__mark"></span><span>MERIDIAN<small>RESTORATION CORP</small></span></div>
  </div>

  <div class="panel contact">
    <svg class="shape" viewBox="0 0 230 540" aria-hidden="true">
      <path d="M0,0 H230 V22 Q120,48 0,30 Z" fill="var(--teal)"/>
    </svg>
    <div class="contact__message">
      <p class="heading heading--teal">Your company message</p>
      <p class="heading heading--dark">Will Goes Here</p>
    </div>
    <ul class="contact__list">
      <li><span class="icon"><svg viewBox="0 0 12 12"><path d="M2 1h2l1 3-1.3 1a7 7 0 0 0 3.3 3.3L8 7l3 1v2a1 1 0 0 1-1 1A9 9 0 0 1 1 2a1 1 0 0 1 1-1z" fill="#fff"/></svg></span>+01 555 010 2030</li>
      <li><span class="icon"><svg viewBox="0 0 12 12"><rect x="1" y="2.5" width="10" height="7" fill="none" stroke="#fff" stroke-width="1.2"/><path d="M1 3l5 4 5-4" fill="none" stroke="#fff" stroke-width="1.2"/></svg></span>hello@meridianrc.com</li>
      <li><span class="icon"><svg viewBox="0 0 12 12"><circle cx="6" cy="6" r="4.6" fill="none" stroke="#fff" stroke-width="1.1"/><path d="M1.4 6h9.2M6 1.4c-2.4 3-2.4 6.2 0 9.2M6 1.4c2.4 3 2.4 6.2 0 9.2" fill="none" stroke="#fff" stroke-width=".9"/></svg></span>meridianrc.com</li>
      <li><span class="icon"><svg viewBox="0 0 12 12"><path d="M6 11S2 6.8 2 4.5a4 4 0 0 1 8 0C10 6.8 6 11 6 11z" fill="#fff"/><circle cx="6" cy="4.5" r="1.4" fill="var(--teal)"/></svg></span>48 Harbor Lane, Suite 12</li>
    </ul>
    <div class="photo contact__map" role="img" aria-label="Soft grey backdrop of a city skyline"></div>
  </div>

  <div class="panel cover">
    <svg class="shape" viewBox="0 0 230 540" aria-hidden="true">
      <rect width="230" height="150" fill="var(--black)"/>
      <polygon points="150,150 230,110 230,175" fill="var(--teal)"/>
    </svg>
    <div class="brand"><span class="brand__mark"></span><span>MERIDIAN<small>RESTORATION CORP</small></span></div>
    <div class="photo cover__photo" role="img" aria-label="Aerial photo of high-rise towers in a downtown district"></div>
    <div class="cover__headline">
      <p class="heading heading--teal">Your Headline</p>
      <p class="heading heading--dark">Will Goes Here</p>
    </div>
    <div class="cover__web">www.meridianrestoration.com</div>
  </div>
</section>

<!-- Inside of the brochure -->
<section class="spread spread--inside">
  <div class="panel intro">
    <svg class="shape" viewBox="0 0 230 540" aria-hidden="true">
      <rect width="230" height="200" fill="var(--teal)"/>
    </svg>
    <div class="photo intro__building" role="img" aria-label="Residential high-rise with balconies, blue glazing and planted terraces"></div>
    <svg class="shape" viewBox="0 0 230 540" aria-hidden="true">
      <polygon points="0,160 230,160 230,200 0,250" fill="var(--teal)"/>
      <polygon points="0,200 90,232 0,258" fill="var(--black)"/>
    </svg>
    <div class="intro__text">
      <p class="body-copy">This is a short introduction to our services. We restore concrete, envelopes and garages for residential owners, boards and property managers. Our team combines field experience, clear reporting and safe methods on every site we touch, from small repairs to full programs.</p>
    </div>
  </div>

  <div class="panel services">
    <div class="services__group">
      <h3 class="heading section-title">Building Envelope</h3>
      <div class="services__cols">
        <div class="services__col">
          <span class="pill">Concrete Repairs</span>
          <p class="item"><span class="item__num">1</span>Balcony Slabs</p>
          <p class="item"><span class="item__num">2</span>Plaza Walls</p>
          <p class="item"><span class="item__num">3</span>Plazas &amp; Exteriors</p>
          <span class="pill">Waterproofing</span>
          <p class="item"><span class="item__num">4</span>Window and caulking</p>
          <p class="item"><span class="item__num">5</span>Masonry repairs</p>
          <p class="item"><span class="item__num">6</span>Balcony membrane joints</p>
        </div>
        <div class="services__col">
          <p class="item"><span class="item__num">7</span>Railing replacement</p>
          <p class="item"><span class="item__num">8</span>Sub-grade waterproofing</p>
          <p class="item"><span class="item__num">9</span>Roof deck coatings</p>
          <span class="pill">Structural</span>
          <p class="item"><span class="item__num">10</span>Repairs &amp; Retrofits</p>
          <p class="item"><span class="item__num">11</span>Garage &amp; Podium slabs</p>
        </div>
      </div>
    </div>
    <div class="services__group">
      <h3 class="heading section-title">Parking Garage Structures</h3>
      <div class="services__cols">
        <div class="services__col">
          <span class="pill">Concrete Repairs</span>
          <p class="item"><span class="item__num">1</span>Partial slab replacement</p>
          <p class="item"><span class="item__num">2</span>Column repairs</p>
          <p class="item"><span class="item__num">3</span>Traffic coatings</p>
          <p class="item"><span class="item__num">4</span>Ramp &amp; beam repairs</p>
          <span class="pill">Ramp Renovation</span>
          <p class="item"><span class="item__num">5</span>Electric heating cables</p>
          <p class="item"><span class="item__num">6</span>Asphalt and concrete</p>
        </div>
        <div class="services__col">
          <p class="item"><span class="item__num">7</span>Expansion joints</p>
          <p class="item"><span class="item__num">8</span>Structural strengthening</p>
          <p class="item"><span class="item__num">9</span>Drainage upgrades</p>
          <p class="item"><span class="item__num">10</span>Mastic waterproofing</p>
          <p class="item"><span class="item__num">11</span>Foundation wall cracks</p>
          <p class="item"><span class="item__num">12</span>Crystalline waterproofing</p>
        </div>
      </div>
    </div>
  </div>

  <div class="panel misc">
    <h3 class="heading section-title">Miscellaneous</h3>
    <ul class="misc__list">
      <li>Site inspections and condition reports</li>
      <li>Line painting and garage signage</li>
      <li>Sealants, epoxy and crack injection</li>
      <li>Emergency repairs available</li>
    </ul>
    <div class="photo misc__photo" role="img" aria-label="Underground parking garage with columns, beams and parked cars"></div>
    <p class="body-copy misc__text">Our garage teams keep structures open while work proceeds, phasing repairs to protect residents, vehicles and access.</p>
    <svg class="shape" viewBox="0 0 230 540" aria-hidden="true">
      <polygon points="230,440 230,540 120,540" fill="var(--black)"/>
      <polygon points="230,470 230,540 170,540" fill="var(--teal)"/>
    </svg>
  </div>
</section>

</body>
</html>
```